Business Card Design Project

We have a logo design and are now looking for a business card design. We supply pre-construction services to the Wireless Telecommunication Industry in the development of cell phone tower and other antenna supporting infrastructure e.g. buildings. The types of services include Real Estate Leasing, Zoning & Permitting,Surveying and A&E work. I am looking for a card that includes the logo we have selected along with the full company name. Company colors are Blue and Silver. I want something professional and that "pops". Use your imagination with the four sided star portion of the logo - it can be stretched such that it occupies a large portion of the card or kept simple the way it is. I am interested in seeing the design on a white, silver, navy, black or charcoal background or any other color you think works well with the logo. Apart from the logo that includes HRM we also need to see the full company name on the card - Harborline Relay Maintenance, Inc. The design must also show a persons name, title, address, (2) phone numbers, e-mail address and web address www.hrm.example

Target Market(s)

Cell phone carriers e.g. Quellport Mobile, BN&K, Zandex Cell, Ovalo etc.

Industry/Entity Type

Cell Phone

Requirements
Must have
• Logo and
Harborline Relay Maintenance, Inc.

```html
<!DOCTYPE html>
<html lang="en">
<head>
<meta charset="utf-8">
<title>HRM Business Card</title>
<link href="https://fonts.googleapis.com/css2?family=Cinzel:wght@600&family=Didact+Gothic&display=swap" rel="stylesheet">
<style>
  :root {
    --page: #d9d8d4;
    --card-black: #0c0d0f;
    --card-navy: #0a2236;
    --glow-blue: #1f74b3;
    --brand-blue: #2a9be0;
    --silver: #c9cbcd;
    --silver-dark: #8e9194;
    --text-light: #e6e7e8;
  }
  * { margin: 0; padding: 0; box-sizing: border-box; }
  html, body { width: 1200px; height: 871px; overflow: hidden; }
  body {
    background: var(--page);
    position: relative;
    font-family: "Didact Gothic", "Century Gothic", sans-serif;
  }
  .card {
    position: absolute;
    width: 540px;
    height: 309px;
    overflow: hidden;
    box-shadow: 0 10px 24px rgba(0,0,0,0.35);
  }
  /* Front */
  .card-front {
    left: 70px; top: 90px;
    background:
      radial-gradient(ellipse 260px 170px at 300px 110px, var(--glow-blue) 0%, var(--card-navy) 55%, var(--card-black) 100%);
  }
  .brand {
    position: absolute;
    display: flex;
    align-items: center;
    gap: 14px;
    color: var(--brand-blue);
    font-family: "Didact Gothic", "Century Gothic", sans-serif;
    letter-spacing: 2px;
    line-height: 1;
  }
  .brand-mark {
    border-radius: 50%;
    background: var(--brand-blue);
  }
  .card-front .brand { left: 165px; top: 66px; font-size: 74px; }
  .card-front .brand-mark { width: 34px; height: 34px; }
  .company-name {
    position: absolute;
    color: var(--silver);
    letter-spacing: 1.2px;
    white-space: nowrap;
  }
  .card-front .company-name {
    left: 0; right: 0; top: 160px;
    text-align: center;
    font-size: 15px;
  }
  .front-band {
    position: absolute;
    left: 0; right: 0; top: 222px; height: 34px;
    background: linear-gradient(180deg, #e2e3e4, var(--silver) 60%, var(--silver-dark));
    display: flex; align-items: center; justify-content: center;
  }
  .front-band .web {
    color: #1b6fb0;
    font-size: 17px;
    font-weight: 700;
    letter-spacing: 0.5px;
  }
  .front-base {
    position: absolute;
    left: 0; right: 0; top: 256px; bottom: 0;
    background: linear-gradient(180deg, #3a3d40, #1a1b1d);
  }
  /* Back */
  .card-back {
    left: 590px; top: 472px;
    background: var(--card-black);
  }
  .card-back .brand { left: 34px; top: 100px; font-size: 58px; }
  .card-back .brand-mark { width: 26px; height: 26px; }
  .card-back .company-name {
    left: 34px; top: 172px;
    font-size: 11.5px;
  }
  .back-bands { position: absolute; left: 0; top: 0; }
  .person { position: absolute; left: 292px; top: 40px; }
  .person-name {
    font-family: "Cinzel", Georgia, serif;
    font-weight: 600;
    color: var(--text-light);
    font-size: 17px;
    letter-spacing: 1px;
  }
  .person-title { color: var(--brand-blue); font-size: 12px; margin-top: 1px; }
  .address {
    position: absolute; left: 292px; top: 100px;
    color: var(--text-light); font-size: 13px; line-height: 17px;
  }
  .contacts {
    position: absolute; left: 292px; top: 150px;
    color: var(--text-light); font-size: 13px; list-style: none;
  }
  .contacts li { display: flex; align-items: center; gap: 18px; height: 19px; }
  .contacts svg { width: 12px; height: 12px; fill: none; stroke: var(--brand-blue); stroke-width: 1.6; }
  .back-web {
    position: absolute; left: 292px; top: 230px;
    color: var(--text-light); font-size: 13px;
  }
</style>
</head>
<body>

<section class="card card-front" aria-label="Card front">
  <div class="brand"><span class="brand-mark"></span>HRM</div>
  <div class="company-name">Harborline Relay Maintenance, Inc.</div>
  <div class="front-band"><span class="web">www.hrm.example</span></div>
  <div class="front-base"></div>
</section>

<section class="card card-back" aria-label="Card back">
  <svg class="back-bands" width="540" height="309" viewBox="0 0 540 309">
    <defs>
      <linearGradient id="silverBand" x1="0" y1="0" x2="0" y2="1">
        <stop offset="0" stop-color="#e3e4e5"/>
        <stop offset="1" stop-color="#9a9da0"/>
      </linearGradient>
    </defs>
    <polygon points="0,236 238,276 250,289 0,252" fill="#2a9be0"/>
    <polygon points="238,276 540,288 540,302 250,289" fill="url(#silverBand)"/>
  </svg>

  <div class="brand"><span class="brand-mark"></span>HRM</div>
  <div class="company-name">Harborline Relay Maintenance, Inc.</div>

  <div class="person">
    <div class="person-name">Dana Whitlow</div>
    <div class="person-title">Ceo</div>
  </div>

  <div class="address">
    Level 4, 210 Harbor Road<br>
    EASTMERE NSW 2999
  </div>

  <ul class="contacts">
    <li>
      <svg viewBox="0 0 12 12"><path d="M2 4c0-2 8-2 8 0M3 5h6l1 5H2z"/></svg>
      <span>02 5550 0148</span>
    </li>
    <li>
      <svg viewBox="0 0 12 12"><rect x="3" y="1" width="6" height="3"/><rect x="1" y="4" width="10" height="5"/><rect x="3" y="8" width="6" height="3"/></svg>
      <span>02 5550 0195</span>
    </li>
    <li>
      <svg viewBox="0 0 12 12"><rect x="1" y="2.5" width="10" height="7"/><path d="M1 2.5l5 4 5-4"/></svg>
      <span>dana@hrm.example</span>
    </li>
  </ul>

  <div class="back-web">www.hrm.example</div>
</section>

</body>
</html>
```